TRUCKING/TRANSPORTATION COMPANY BUSINESS CARD.

We need a business card design for our trucking company based in Fenwick, AL.
It will be a double sided design.
FRONT SIDE:
We need a good looking logo with a tagline. The tagline should match the type of business.
COMPANY NAME: DW HAULAGE LLC
BACK SIDE:
The following information should be displayed on the back of the card.
Office: 555.274.1968
Mailing: 214 W. Birch Ave.
Fenwick, AL 38921
Email: dwhaulllc@mailbox-example.net
Trucking Company
FRONT SIDE:
BACK SIDE:
Office: 555.274.1968
Mailing: 214 W. Birch Ave.
Fenwick, AL 38921

```html
<!DOCTYPE html>
<html lang="en">
<head>
<meta charset="utf-8">
<title>DW Haulage LLC – Business Card</title>
<link rel="stylesheet" href="https://fonts.googleapis.com/css2?family=Oswald:wght@400;500;600&display=swap">
<style>
  :root {
    --stage: #1a1a1b;
    --card-light: #f2f2f2;
    --card-dark: #161718;
    --card-dark-edge: #222426;
    --brand-blue: #1f74c4;
    --brand-red: #e8202a;
    --ink-grey: #6b6b6b;
    --ink-dark: #4a4a4a;
    --ink-light: #c9c9c9;
  }
  * { box-sizing: border-box; margin: 0; padding: 0; }
  html, body {
    width: 1200px; height: 871px; overflow: hidden;
    background: var(--stage);
    font-family: "Oswald", "Arial Narrow", sans-serif;
  }
  .stage {
    position: relative; width: 1200px; height: 871px;
    display: flex; flex-direction: column; align-items: center; justify-content: center; gap: 56px;
  }
  .card {
    position: relative; width: 600px; height: 343px; overflow: hidden;
    box-shadow: 0 10px 30px rgba(0,0,0,.5);
  }

  /* Back side – contact details */
  .card--back { background: var(--card-light); display: flex; align-items: center; }
  .back__brand {
    width: 250px; display: flex; flex-direction: column; align-items: center; gap: 16px;
  }
  .brand-dot { width: 56px; height: 56px; border-radius: 50%; background: var(--brand-blue); }
  .back__name {
    font-weight: 500; font-size: 20px; letter-spacing: 2px; color: var(--ink-grey);
  }
  .back__divider { width: 3px; height: 210px; background: var(--brand-blue); }
  .back__details { padding-left: 28px; }
  .holder-name { font-weight: 600; font-size: 30px; color: var(--ink-grey); margin-bottom: 10px; }
  .contact { list-style: none; }
  .contact li {
    display: flex; align-items: center; gap: 10px;
    font-weight: 500; font-size: 16px; letter-spacing: .5px; color: var(--ink-dark); line-height: 30px;
    white-space: nowrap;
  }
  .contact svg { width: 16px; height: 16px; fill: var(--brand-blue); flex: none; }

  /* Front side – brand */
  .card--front { background: linear-gradient(160deg, var(--card-dark-edge), var(--card-dark)); }
  .front__accents { position: absolute; inset: 0; }
  .front__brand {
    position: absolute; inset: 0; display: flex; flex-direction: column; align-items: center; justify-content: center;
  }
  .front__brand .brand-dot { width: 84px; height: 84px; margin-bottom: 22px; }
  .front__name {
    font-weight: 500; font-size: 38px; letter-spacing: 4px; color: var(--ink-light); line-height: 1.1;
  }
  .tagline {
    font-weight: 500; font-size: 19px; letter-spacing: 1.5px; color: var(--brand-red); text-transform: uppercase;
  }
</style>
</head>
<body>
<main class="stage">
  <section class="card card--back" aria-label="Business card back">
    <div class="back__brand">
      <span class="brand-dot"></span>
      <span class="back__name">DW HAULAGE LLC</span>
    </div>
    <div class="back__divider"></div>
    <div class="back__details">
      <p class="holder-name">Your Name</p>
      <ul class="contact">
        <li>
          <svg viewBox="0 0 16 16" aria-hidden="true"><path d="M1 6c0-2 3-3 7-3s7 1 7 3v1h-3V5.5C11 5 9.5 5 8 5S5 5 4 5.5V7H1z"/><path d="M4 8h8l2 6H2z"/></svg>
          555.274.1968
        </li>
        <li>
          <svg viewBox="0 0 16 16" aria-hidden="true"><path d="M8 0a5.5 5.5 0 0 0-5.5 5.5C2.5 10 8 16 8 16s5.5-6 5.5-10.5A5.5 5.5 0 0 0 8 0zm0 8a2.5 2.5 0 1 1 0-5 2.5 2.5 0 0 1 0 5z"/></svg>
          214 W. Birch Ave. Fenwick, AL 38921
        </li>
        <li>
          <svg viewBox="0 0 16 16" aria-hidden="true"><path d="M1 3h14v1.5L8 9 1 4.5z"/><path d="M1 6l7 4.5L15 6v7H1z"/></svg>
          dwhaulllc@mailbox-example.net
        </li>
      </ul>
    </div>
  </section>

  <section class="card card--front" aria-label="Business card front">
    <svg class="front__accents" viewBox="0 0 600 343" aria-hidden="true">
      <polygon points="0,0 300,0 0,44" fill="var(--brand-blue)"/>
      <polygon points="600,343 600,292 330,343" fill="var(--brand-red)"/>
    </svg>
    <div class="front__brand">
      <span class="brand-dot"></span>
      <p class="front__name">DW HAULAGE LLC</p>
      <p class="tagline">Dependable on every route</p>
    </div>
  </section>
</main>
</body>
</html>
```